Supplement Company Needs A New Label Design

My company is looking to increase the appeal of our supplement labels. We need to keep the logo the same, the name the same, and the overall information all the same. We wouldn't mind adding the following, or changing colour schemes/fonts to increase shelf appeal.

Helps To:

- Increase Bioavailability of Nutrients

- Regulate Blood Sugar Levels

- Reduce Body Fat

- Increase Insulin Sensitivity

The label needs to be roughly 3inches high and 8inches around.

About Us:
Scientifically backed formulas with studies linked back to each ingredient. No "proprietary blends" just pure transparency.

We have another product that will need to be done too, so the winner could be chosen for the secondary project as well.

Target Market(s)

Those looking to lose weight and regulate their blood sugar. This product can be used from those looking to pack muscle on while losing fat, or by diabetics looking to control blood sugar and weight.

Industry/Entity Type

Supplement

Requirements
Must have
• My project must have an appeal that draws people when they see it on a shelf. Something that will differentiate it from my competitors. It must also have "Helps to" if including the things it does. This is just to follow QHW guidelines.
Nice to have
• Nice to have a unique kind of font for the name "Gather and Prevail". I tried my best with designing the labels to give a good template to use, however, this is all I am capable of.

```html
<!DOCTYPE html>
<html lang="en">
<head>
<meta charset="UTF-8">
<title>Gather &amp; Prevail – Nutrient Partitioner Label</title>
<link href="https://fonts.googleapis.com/css2?family=Oswald:wght@300;400&display=swap" rel="stylesheet">
<style>
  :root {
    --backdrop: #ececec;
    --navy-deep: #0f1f36;
    --navy: #16305a;
    --band-bright: #2a7fd4;
    --band-mid: #1b62b8;
    --band-dark: #143c72;
    --label-text: #f2f4f7;
  }
  * { margin: 0; padding: 0; box-sizing: border-box; }
  html, body {
    width: 1200px;
    height: 900px;
    overflow: hidden;
    background: var(--backdrop);
  }
  .canvas {
    position: relative;
    width: 1200px;
    height: 900px;
    display: flex;
    align-items: center;
    justify-content: center;
  }
  .label {
    position: relative;
    width: 480px;
    height: 790px;
    background: linear-gradient(160deg, var(--navy) 0%, var(--navy-deep) 60%, #0c1a2e 100%);
    overflow: hidden;
    font-family: "Oswald", "Arial Narrow", sans-serif;
    font-weight: 300;
    color: var(--label-text);
    text-align: center;
  }
  .band {
    position: absolute;
    left: 0;
    width: 100%;
  }
  .band-top {
    top: 0;
    height: 150px;
    background: linear-gradient(180deg, var(--band-mid) 0%, var(--band-dark) 55%, rgba(22, 48, 90, 0) 100%);
  }
  .band-bottom {
    bottom: 0;
    height: 70px;
    background: linear-gradient(0deg, var(--band-dark) 0%, var(--band-mid) 55%, rgba(15, 31, 54, 0) 100%);
  }
  .label-content {
    position: absolute;
    top: 185px;
    left: 0;
    width: 100%;
    display: flex;
    flex-direction: column;
    align-items: center;
  }
  .product-name {
    font-weight: 300;
    font-size: 96px;
    line-height: 1.02;
    letter-spacing: 2px;
    font-variant: small-caps;
  }
  .tagline {
    margin-top: 40px;
    font-size: 24px;
    line-height: 1.7;
    font-variant: small-caps;
    letter-spacing: 0.5px;
  }
  .product-type {
    margin-top: 22px;
    font-size: 24px;
    font-variant: small-caps;
    letter-spacing: 0.5px;
  }
  .brand-name {
    margin-top: 44px;
    font-size: 26px;
    line-height: 1.5;
    letter-spacing: 1px;
    text-transform: uppercase;
  }
</style>
</head>
<body>
<main class="canvas">
  <section class="label">
    <div class="band band-top" role="img" aria-label="Decorative blue wave band across the top of the label"></div>

    <div class="label-content">
      <h1 class="product-name">Gather &amp;<br>Prevail</h1>
      <p class="tagline">For those who want to take control<br>of body transformation</p>
      <p class="product-type">Nutrient Partitioner</p>
      <p class="brand-name">Solen<br>Nutrivex</p>
    </div>

    <div class="band band-bottom" role="img" aria-label="Decorative blue wave band along the bottom of the label"></div>
  </section>
</main>
</body>
</html>
```